Stylish High End Wedding Videography/Films Website (BMTS)

We need a modern and high-end website look for our wedding video and films business. We films weddings all over the United Kingdom and at European destinations so need something to reflect our work. The website should be visually stunning with images and videos being the focal point as this is what our services are;

I have uploads of some items I like and the features the site needs to have. These have been taken from other websites using standout features.

We need the following pages;

1 - Homepage
2 - Films Index Page
3 - Individual Films Page
4 - Prices / Collection Page
5 - Reviews
6 - Options
7 - About
8 - Contact
9 - Blog Index
10 - Blog Page

All pages must be consistent so have a similar style.

Pages on menu:
Films
Prices
Reviews
Options
About
Contact

We require a responsive look too. Over 90% of our visitors access the website via their mobile devices.

Please use the colours from our logo to incorporate into the website.

Target Market(s)

Wedding Couples

Industry/Entity Type

Wedding Photography

Number of Pages Required

5+ page

Font styles to use
Sans Serif
Script

Requirements
Must have
• The logo must be in the centre of the menu at the top.

Social icons at the bottom of the page.

Use only two fonts including Lore which is supplied
Nice to have
• Different video for each page on the top header. This will play behind the menu.

```html
<!DOCTYPE html>
<html lang="en">
<head>
<meta charset="utf-8">
<title>Elwyn Marsh Films – Wedding Videography</title>
<link rel="stylesheet" href="https://fonts.googleapis.com/css2?family=Lora:wght@400;700&family=Poppins:wght@400;500;600&display=swap">
<style>
:root{
  --gold:#a8904c;
  --gold-dark:#8f7a3e;
  --paper:#f4f4f4;
  --white:#ffffff;
  --ink:#262626;
  --muted:#6b6b6b;
  --night:#1c1a17;
  --serif:'Lora', Georgia, serif;
  --sans:'Poppins', Arial, sans-serif;
}
*{box-sizing:border-box;margin:0;padding:0}
html,body{width:1200px;height:4594px;overflow:hidden}
body{position:relative;background:var(--white);color:var(--ink);font-family:var(--sans)}
.abs{position:absolute}
.photo{position:absolute;display:block}
.band{position:absolute;left:0;width:1200px}

/* header */
.hero{top:0;height:704px;background:var(--paper)}
.brand{position:absolute;font-family:var(--sans);font-weight:600;color:var(--ink);letter-spacing:4px;font-size:15px;white-space:nowrap}
.brand-dot{display:inline-block;width:12px;height:12px;border-radius:50%;background:var(--gold);margin-right:10px;vertical-align:-1px}
.menu-brand{left:0;width:1200px;top:50px;text-align:center}
.nav{position:absolute;top:53px;font-family:var(--serif);font-size:12px;letter-spacing:.5px;color:var(--ink);white-space:nowrap}
.nav.active{color:var(--gold)}
.hero-title{left:162px;top:212px;font-family:var(--serif);font-weight:700;font-size:55px;line-height:63px;color:#111}
.hero-sub{left:162px;top:417px;width:370px;font-size:13.5px;line-height:22px;color:#333;letter-spacing:.3px}
.btn{position:absolute;background:var(--gold);color:var(--white);font-family:var(--serif);font-weight:700;font-size:12.5px;letter-spacing:.5px;display:flex;align-items:center;justify-content:center}

/* about */
.about-text{left:290px;top:838px;width:620px;text-align:center;font-family:var(--serif);font-size:16.5px;line-height:27px;color:#333}
.kicker{position:absolute;font-size:11px;font-weight:600;letter-spacing:4px;color:var(--gold);text-transform:uppercase;white-space:nowrap}

/* testimonial */
.quote-band{top:1706px;height:418px;background:linear-gradient(100deg,#171513 0%,#2a2520 45%,#3a3128 70%,#1d1a16 100%)}
.quote-mark{left:160px;top:1760px;font-family:var(--serif);font-weight:700;font-size:64px;color:var(--white);line-height:1}
.quote-text{left:162px;top:1834px;width:640px;font-family:var(--serif);font-size:14.5px;line-height:22.5px;color:#eee}
.dots{left:162px;top:2037px;display:flex;gap:13px}
.dots span{width:9px;height:9px;background:var(--white)}
.dots span.on{background:var(--gold)}

/* films */
.films-band{top:2124px;height:627px;background:var(--paper)}
.card{position:absolute;background:var(--white)}
.h2{position:absolute;font-family:var(--serif);font-weight:700;font-size:39px;color:#111}
.gold-sub{position:absolute;font-size:12px;font-weight:500;line-height:23px;color:var(--gold)}
.body-small{position:absolute;font-size:12px;line-height:22.5px;color:#555}

/* stories */
.stories-text{left:250px;top:2872px;width:700px;text-align:center;font-family:var(--serif);font-size:16.5px;line-height:27px;color:#333}
.story-title{position:absolute;font-family:var(--serif);font-size:11.5px;color:#222;letter-spacing:.2px;white-space:nowrap}
.story-desc{position:absolute;width:195px;font-size:10.5px;line-height:18px;color:#666}

/* call band */
.call-band{top:3388px;height:150px;background:var(--gold)}
.call-label{left:162px;top:3446px;font-family:var(--serif);font-size:25px;color:var(--white);letter-spacing:.5px;white-space:nowrap}
.call-number{left:340px;top:3442px;font-family:var(--serif);font-weight:700;font-size:28px;color:var(--white);white-space:nowrap}
.call-mark{left:566px;top:3450px;width:140px;text-align:center;font-family:var(--serif);font-weight:700;font-size:16px;letter-spacing:2px;color:var(--white);white-space:nowrap}
.call-info{left:713px;top:3424px;width:300px;font-size:11px;line-height:18px;color:var(--white);letter-spacing:.3px}
.call-mail{left:713px;top:3471px;font-family:var(--serif);font-weight:700;font-size:13px;color:var(--white);display:flex;align-items:center;gap:10px;white-space:nowrap}

/* contact */
.contact-band{top:3538px;height:625px;background:var(--paper)}
.field{position:absolute;width:171px;height:30px;border-bottom:1px solid #cfcfcf;font-size:10.5px;color:#777;padding-top:4px}
.field.wide{width:358px;height:44px}

/* instagram */
.insta-band{top:4163px;height:148px;background:linear-gradient(90deg,#2c2a2a,#3a3330 25%,#2b2c31 50%,#3b332e 75%,#2a2726)}
.insta-btn{left:469px;top:4206px;width:262px;height:59px;background:var(--white);display:flex;align-items:center;justify-content:center;gap:10px;font-family:var(--serif);font-weight:700;font-size:14px;color:#111;letter-spacing:.3px}
.insta-btn i{width:14px;height:14px;border:1.6px solid #111;border-radius:50%}

/* footer */
.fnav{position:absolute;top:4458px;font-family:var(--serif);font-size:12px;color:#666}
.fnav.active{color:var(--gold)}
.social{position:absolute;top:4488px;width:36px;height:36px;border-radius:50%;background:#ececec}
.social.on{background:var(--gold)}
.copyright{left:0;top:4549px;width:1200px;text-align:center;font-size:10px;color:#777}
.copyright b{color:var(--gold);font-weight:400}
</style>
</head>
<body>

<!-- Hero -->
<section class="band hero"></section>
<a class="nav active" style="left:268px">HOME</a>
<a class="nav" style="left:342px">FILMS</a>
<a class="nav" style="left:414px">PRICES</a>
<div class="brand menu-brand"><span class="brand-dot"></span>ELWYN MARSH</div>
<a class="nav" style="left:718px">REVIEWS</a>
<a class="nav" style="left:804px">OPTIONS</a>
<a class="nav" style="left:890px">ABOUT</a>
<a class="nav" style="left:964px">CONTACT</a>

<h1 class="abs hero-title">Create a<br>beautiful<br>wedding films</h1>
<p class="abs hero-sub">WEDDING VIDEOGRAPHY – NORTH EAST, UK AND WORLDWIDE FILMS</p>
<a class="btn" style="left:162px;top:480px;width:155px;height:44px">CONTACT US</a>

<div class="photo" role="img" aria-label="Close-up of a pale pink flower with green leaves" style="left:727px;top:157px;width:150px;height:110px;background:linear-gradient(135deg,#5b6b3e,#c9a9a0 50%,#4f5a33)"></div>
<div class="photo" role="img" aria-label="Bride and groom holding hands against dark green foliage" style="left:915px;top:100px;width:224px;height:167px;background:linear-gradient(120deg,#1f2a1a,#5e6d3a 50%,#2b2e22)"></div>
<div class="photo" role="img" aria-label="Red and pink bridal bouquet on a white background" style="left:565px;top:307px;width:225px;height:283px;background:radial-gradient(circle at 50% 40%,#b4243a 0%,#d5657a 30%,#f2eeee 65%)"></div>
<div class="photo" role="img" aria-label="Couple embracing among mossy rocks" style="left:827px;top:307px;width:278px;height:351px;background:linear-gradient(160deg,#4a4a3a,#8a8570 45%,#3c3a2c)"></div>
<div class="photo" role="img" aria-label="Woodland wedding scene" style="left:1139px;top:403px;width:61px;height:139px;background:linear-gradient(180deg,#6b5a3a,#3a3020)"></div>

<!-- About -->
<div class="abs" style="left:599px;top:704px;width:1px;height:80px;background:var(--gold)"></div>
<div class="abs" style="left:591px;top:784px;width:17px;height:17px;border-radius:50%;background:var(--gold)"></div>
<p class="abs about-text">Elwyn Marsh is a wedding filmmaker based in the North East of England. We film weddings in a fun and natural way. All weddings are totally unique to the couple. If you are looking for a wedding film for your special day we'd love to hear from you.</p>
<a class="kicker" style="left:0;width:1200px;text-align:center;top:974px">About us</a>

<div class="photo" role="img" aria-label="Bride holding a white bouquet of flowers" style="left:162px;top:1052px;width:277px;height:276px;background:linear-gradient(150deg,#c9b9a0,#8f7a5c 45%,#e8e4dc)"></div>
<div class="photo" role="img" aria-label="Couple touching foreheads in a sepia misty landscape" style="left:462px;top:1052px;width:276px;height:276px;background:linear-gradient(180deg,#e6cba6,#c9a47a 60%,#8a6c4e)"></div>
<div class="photo" role="img" aria-label="Newlyweds celebrating down the aisle" style="left:761px;top:1052px;width:277px;height:276px;background:linear-gradient(160deg,#6a5138,#b59a7a 50%,#e8e2da)"></div>
<div class="photo" role="img" aria-label="Bride throwing the bouquet to guests" style="left:162px;top:1352px;width:382px;height:276px;background:linear-gradient(170deg,#6a5a46,#3c3028 50%,#8a7560)"></div>
<div class="photo" role="img" aria-label="Smiling bride with a baby's breath bouquet on brick paving" style="left:567px;top:1352px;width:471px;height:276px;background:linear-gradient(135deg,#9a7a66,#e4dcd6 45%,#b08c74)"></div>

<!-- Testimonial -->
<section class="band quote-band" role="img" aria-label="Dim photograph of a bride and groom in a garden"></section>
<div class="abs quote-mark">“</div>
<p class="abs quote-text">One of the best decisions We made was choosing you guys to film our wedding! It's absolutely fantastic, it has everyone so emotional watching it, we can't thank you enough for capturing our special day! You were amazing from start to finish<br><br>Thanks so much.</p>
<div class="kicker" style="left:162px;top:1978px;font-size:11px">- Laura and Daniel</div>
<div class="abs" style="left:180px;top:1998px;font-size:12px;color:var(--white)">The Mill Barn Hexham</div>
<div class="abs dots"><span></span><span class="on"></span><span></span></div>

<!-- Films -->
<section class="band films-band"></section>
<div class="photo" role="img" aria-label="Groom kissing the bride's cheek in an ornate hall" style="left:162px;top:2199px;width:450px;height:438px;background:linear-gradient(120deg,#5a4226,#a9895c 40%,#efe9e2 70%,#c9b59a)"></div>
<div class="card" style="left:588px;top:2238px;width:450px;height:437px"></div>
<h2 class="h2" style="left:633px;top:2277px">Films</h2>
<p class="gold-sub" style="left:633px;top:2330px">I'd love to hear from you if you are getting married.<br>Please fill in the form below to check my availability.</p>
<p class="body-small" style="left:633px;top:2400px;width:350px">Lorem Ipsum is simply dummy text of the printing and typesetting industry. Lorem Ipsum has been the industry's standard dummy text ever since the 1500s, when an unknown printer took a galley of type and scrambled it to make a type specimen book.</p>
<a class="btn" style="left:631px;top:2550px;width:173px;height:44px">WEDDING VIDEOS</a>
<a class="kicker" style="left:494px;top:2648px">+ Prices</a>

<!-- Stories -->
<h2 class="h2" style="left:0;width:1200px;text-align:center;top:2817px">Stories</h2>
<p class="abs stories-text">Your wedding day is a once in a lifetime moment. A moment in time where all the people you love and care about are in the same place at the same time. We document unique moments on film. The laughs, the tears and the love.</p>
<a class="kicker" style="left:0;width:1200px;text-align:center;top:2976px">Discover more</a>

<div class="photo" role="img" aria-label="Bride in a veil with the groom behind" style="left:162px;top:3029px;width:195px;height:195px;background:linear-gradient(120deg,#3a5a7a,#c9ced6 50%,#2a2a2e)"></div>
<div class="photo" role="img" aria-label="Black and white ceremony at the altar" style="left:389px;top:3029px;width:194px;height:195px;background:linear-gradient(160deg,#d8d8d8,#7a7a7a 50%,#2a2a2a)"></div>
<div class="photo" role="img" aria-label="Close-up portrait of a smiling bride" style="left:615px;top:3029px;width:196px;height:195px;background:linear-gradient(140deg,#d9b89a,#a87858 50%,#5a4030)"></div>
<div class="photo" role="img" aria-label="Couple embracing outdoors" style="left:843px;top:3029px;width:195px;height:195px;background:linear-gradient(150deg,#2a3040,#6a7080 50%,#c9c4c0)"></div>

<div class="story-title" style="left:162px;top:3238px">CINEMATIC HIGHLIGHTS FILM</div>
<p class="story-desc" style="left:162px;top:3258px">A highlights film, a harmony of moving imagery, vocals and music, which is unique to you.</p>
<div class="story-title" style="left:389px;top:3238px">CEREMONY AND SPEECHES</div>
<p class="story-desc" style="left:389px;top:3258px">Want to hear the moment you say your vows or I Do or even see your first kiss?</p>
<div class="story-title" style="left:615px;top:3238px">EXTENDED DOCUMENTARY FILM</div>
<p class="story-desc" style="left:615px;top:3258px">The whole story of your wedding from the morning preparations through to just after the first...</p>
<div class="story-title" style="left:843px;top:3238px">OUR STORY FEATURE</div>
<p class="story-desc" style="left:843px;top:3258px">Every wedding has a unique story behind how both of you met. Our Love Story extra is a perfect...</p>

<!-- Call band -->
<section class="band call-band"></section>
<div class="abs call-label">CALL US</div>
<svg class="abs" style="left:290px;top:3440px" width="46" height="46" viewBox="0 0 46 46" aria-hidden="true">
  <circle cx="23" cy="23" r="21" fill="none" stroke="#fff" stroke-width="1.5"/>
  <path d="M16 13c1.5-1 2.6-.6 3.3.8l1.5 3c.6 1.2.3 2-.7 2.8l-1 .8c.9 2.6 3 4.8 5.6 5.7l.8-1c.8-1 1.7-1.3 2.8-.7l3 1.6c1.3.7 1.700 1.8.7 3.2-1.6 2.3-4 2.6-6.6 1.3-4.6-2.3-8-5.8-10.2-10.4C14.1 17 14.2 14.5 16 13z" fill="none" stroke="#fff" stroke-width="1.5"/>
</svg>
<div class="abs call-number">07700 900 418</div>
<div class="abs call-mark">ELWYN MARSH</div>
<p class="abs call-info">WEDDING VIDEOGRAPHY – NORTH EAST, UK AND WORLDWIDE FILMS</p>
<div class="abs call-mail">
  <svg width="16" height="12" viewBox="0 0 16 12" aria-hidden="true"><rect width="16" height="12" rx="1" fill="#fff"/><path d="M1 1l7 5.5L15 1" fill="none" stroke="#a8904c" stroke-width="1.3"/></svg>
  hello@elwynmarshfilms.com
</div>

<!-- Contact -->
<section class="band contact-band"></section>
<div class="photo" role="img" aria-label="Bride and groom walking hand in hand in a garden" style="left:588px;top:3612px;width:450px;height:437px;background:linear-gradient(140deg,#4a5a2a,#8a9a5a 40%,#e8e4da 60%,#3a3a3a)"></div>
<div class="card" style="left:162px;top:3650px;width:450px;height:437px"></div>
<h2 class="h2" style="left:205px;top:3686px">Contact Us</h2>
<p class="gold-sub" style="left:205px;top:3729px;font-weight:400;font-size:11.5px">I'd love to chat more about your wedding...</p>
<div class="field" style="left:205px;top:3776px">First Name</div>
<div class="field" style="left:392px;top:3776px">Surname</div>
<div class="field" style="left:205px;top:3821px">What your partner's name?</div>
<div class="field" style="left:392px;top:3821px">Email Address</div>
<div class="field" style="left:205px;top:3866px">Mobile No.</div>
<div class="field" style="left:392px;top:3866px">Select Date
  <svg style="position:absolute;right:2px;top:5px" width="13" height="12" viewBox="0 0 13 12" aria-hidden="true"><rect x=".5" y="1.5" width="12" height="10" fill="none" stroke="#999"/><line x1=".5" y1="4.5" x2="12.5" y2="4.5" stroke="#999"/></svg>
</div>
<div class="field wide" style="left:205px;top:3911px">I'd love to know how you met. Tell me your story...</div>
<a class="btn" style="left:205px;top:3982px;width:171px;height:42px">SEND STORY</a>

<!-- Instagram -->
<section class="band insta-band" role="img" aria-label="Strip of recent wedding photographs"></section>
<a class="abs insta-btn"><i></i>ELWYNMARSHFILMS</a>

<!-- Footer -->
<div class="brand" style="left:0;width:1200px;text-align:center;top:4375px"><span class="brand-dot"></span>ELWYN MARSH</div>
<a class="fnav active" style="left:285px">HOME</a>
<a class="fnav" style="left:362px">FILMS</a>
<a class="fnav" style="left:440px">PRICES</a>
<a class="fnav" style="left:522px">REVIEWS</a>
<a class="fnav" style="left:616px">OPTIONS</a>
<a class="fnav" style="left:714px">ABOUT</a>
<a class="fnav" style="left:797px">CONTACT</a>
<a class="social" style="left:528px" aria-label="Social link"></a>
<a class="social on" style="left:581px" aria-label="Social link"></a>
<a class="social" style="left:635px" aria-label="Social link"></a>
<p class="abs copyright">© <b>ELWYN MARSH</b> – 2020. All Rights Reserved</p>

</body>
</html>
```